Business Card design for construction company

I would like a business card design for a construction company - ORD Builders. I have attached the ai logo file for use. I would like the card to be very smart and clean and incorporate only white and the two colours in the logo. I would like the card to have two sides. One side can just have the logo, the other with the relevant information.

Target Market(s)

Building and Construction Clients

Industry/Entity Type

Business

Contact Information for Business Card

Name: Tom Harcliffe
Company: ORD Builders Pty Limited
Address: 14 Mulberry Crescent Oakvale Heights 2093
Phone: 0432 517 208
Email: tomh@ordbuilders.example.au

Font styles to use
Serif
Sans Serif

Requirements
Must have
• Details noted above
• Logo as provided
• Colours as in logo
• Square edges
• A font that compliments the logo
Should not have
• Any colour other than white and those in logo
• Rounded edges

```html
<!DOCTYPE html>
<html lang="en">
<head>
<meta charset="utf-8">
<title>ORD Builders – Business Card</title>
<link rel="stylesheet" href="https://fonts.googleapis.com/css2?family=Open+Sans:wght@400;700&display=swap">
<style>
  :root {
    --backdrop: #ebe8e3;
    --kraft-light: #c4a77c;
    --kraft: #b8996c;
    --kraft-dark: #a98a5e;
    --ink: #141210;
  }
  html, body {
    margin: 0;
    padding: 0;
    width: 1200px;
    height: 900px;
    overflow: hidden;
    background: var(--backdrop);
    font-family: "Open Sans", Arial, sans-serif;
    color: var(--ink);
  }
  .canvas {
    position: relative;
    width: 1200px;
    height: 900px;
  }
  .card {
    position: absolute;
    width: 556px;
    height: 342px;
    background: linear-gradient(160deg, var(--kraft-light) 0%, var(--kraft) 55%, var(--kraft-dark) 100%);
    box-shadow: 0 6px 18px rgba(0, 0, 0, 0.18);
    box-sizing: border-box;
  }
  .card--details {
    left: 238px;
    top: 62px;
  }
  .card--brand {
    left: 458px;
    top: 518px;
    display: flex;
    align-items: center;
    justify-content: center;
  }
  .details {
    position: absolute;
    left: 0;
    right: 0;
    top: 103px;
    text-align: center;
  }
  .details__name {
    margin: 0;
    font-size: 17px;
    font-weight: 700;
    letter-spacing: 0.2px;
    line-height: 22px;
    text-transform: uppercase;
  }
  .details__rule {
    width: 80px;
    height: 1px;
    margin: 13px auto 12px;
    background: var(--ink);
    opacity: 0.7;
  }
  .details__contact,
  .details__company {
    margin: 0;
    font-size: 15.5px;
    line-height: 23px;
  }
  .details__company {
    font-size: 14px;
    line-height: 20px;
  }
  .details__label {
    font-weight: 700;
  }
  .brand-name {
    margin: 0;
    font-size: 40px;
    font-weight: 400;
    letter-spacing: 5px;
    text-transform: uppercase;
    color: var(--ink);
  }
</style>
</head>
<body>
  <main class="canvas">
    <section class="card card--details" aria-label="Business card, contact side">
      <div class="details">
        <h1 class="details__name">Tom Harcliffe</h1>
        <div class="details__rule"></div>
        <p class="details__contact"><span class="details__label">P:</span> 0432 517 208</p>
        <p class="details__contact"><span class="details__label">E:</span> tomh@ordbuilders.example.au</p>
        <div class="details__rule" style="margin-top:9px;margin-bottom:9px"></div>
        <p class="details__company">ORD Builders Pty Limited</p>
        <p class="details__company">14 Mulberry Crescent Oakvale Heights 2093</p>
      </div>
    </section>

    <section class="card card--brand" aria-label="Business card, brand side">
      <p class="brand-name">ORD Builders</p>
    </section>
  </main>
</body>
</html>
```